Business Card Design needed for logo design project

Would like a professional business card for a company involved in financial and latest technologies including CAD design. We would like the card to convey professionalism and communicate that we are involved in up to date technology solutions.

Target Market(s)

Business 2 Business sales

Industry/Entity Type

Financial

Colors

Designer to choose colors to be used in the design.

Requirements
Must have
• Business Name
Logo
Name
Phone
Email
Nice to have
• Website

```html
<!DOCTYPE html>
<html lang="en">
<head>
<meta charset="utf-8">
<title>VANTREX Business Card</title>
<link rel="stylesheet" href="https://fonts.googleapis.com/css2?family=PT+Sans:wght@400;700&display=swap">
<style>
  :root {
    --brand-red: #cc1f27;
    --brand-navy: #0d1a45;
    --paper: #ffffff;
    --stage: #d6d6d6;
    --ink: #141a2e;
    --rule: #5b6277;
  }
  * { box-sizing: border-box; margin: 0; padding: 0; }
  html, body {
    width: 1200px; height: 900px; overflow: hidden;
    background: var(--stage);
    font-family: "PT Sans", Arial, sans-serif;
    color: var(--ink);
  }
  .canvas { position: relative; width: 1200px; height: 900px; }

  .brand-mark {
    position: absolute; top: 55px; left: 0; width: 1200px;
    display: flex; justify-content: center; align-items: center; gap: 24px;
  }
  .brand-mark__name {
    font-weight: 700; font-size: 150px; letter-spacing: 6px;
    color: var(--brand-red); line-height: 1;
  }
  .brand-mark__square {
    width: 48px; height: 48px; background: var(--brand-navy);
  }

  .card {
    position: absolute; top: 320px; width: 540px; height: 310px;
    border-radius: 22px; overflow: hidden;
    box-shadow: 0 8px 18px rgba(0,0,0,0.18);
  }

  /* Front */
  .card--front { left: 30px; background: var(--brand-red); }
  .card--front .card__logo {
    position: absolute; left: 70px; top: 120px;
    font-weight: 700; font-size: 64px; letter-spacing: 3px;
    color: var(--paper); line-height: 1;
  }
  .card__web-band {
    position: absolute; left: 0; right: 0; top: 240px; height: 40px;
    background: linear-gradient(90deg, rgba(13,26,69,0) 0%, rgba(13,26,69,0.55) 25%, var(--brand-navy) 45%);
  }
  .card__web-band span {
    position: absolute; right: 30px; top: 7px;
    font-size: 21px; color: var(--paper);
  }

  /* Back */
  .card--back { left: 630px; background: var(--paper); }
  .card--back .card__logo {
    position: absolute; left: 40px; top: 70px;
    font-weight: 700; font-size: 48px; letter-spacing: 2px;
    color: var(--brand-red); line-height: 1;
  }
  .card__rule {
    position: absolute; left: 0; top: 168px; width: 430px; height: 1.5px;
    background: var(--rule);
  }
  .card__holder { position: absolute; right: 30px; top: 132px; text-align: left; }
  .card__holder-name { font-size: 21px; color: var(--ink); line-height: 1.1; }
  .card__holder-role { font-size: 15px; color: var(--brand-red); line-height: 1.2; }
  .card__tab {
    position: absolute; right: 0; top: 136px; width: 14px; height: 38px;
    background: var(--brand-red);
  }
  .contact-list {
    position: absolute; left: 36px; top: 202px; list-style: none;
  }
  .contact-list li {
    display: flex; align-items: center; gap: 14px;
    font-size: 17px; line-height: 21px;
  }
  .contact-list svg { width: 12px; height: 12px; fill: var(--brand-red); }
  .card__address {
    position: absolute; right: 22px; top: 222px;
    text-align: right; font-size: 13.5px; line-height: 19px;
  }
  .card__base {
    position: absolute; left: 0; right: 0; bottom: 0; height: 22px;
    background: var(--brand-navy);
  }
  .card__base-accent {
    position: absolute; right: 0; bottom: 0; width: 46px; height: 22px;
    background: var(--brand-red);
  }
</style>
</head>
<body>
<main class="canvas">
  <div class="brand-mark">
    <span class="brand-mark__name">VANTREX</span>
    <span class="brand-mark__square"></span>
  </div>

  <section class="card card--front">
    <div class="card__logo">VANTREX</div>
    <div class="card__web-band"><span>www.yourwebsite.com</span></div>
  </section>

  <section class="card card--back">
    <div class="card__logo">VANTREX</div>
    <div class="card__rule"></div>
    <div class="card__holder">
      <div class="card__holder-name">Name here</div>
      <div class="card__holder-role">Designation</div>
    </div>
    <div class="card__tab"></div>
    <ul class="contact-list">
      <li><svg viewBox="0 0 12 12"><path d="M1 4c0-2 2-3 5-3s5 1 5 3l-2 1-1-2H4L3 5zM2 6h8l1 5H1z"/></svg>0123 456 789</li>
      <li><svg viewBox="0 0 12 12"><path d="M3 0h6a1 1 0 0 1 1 1v10a1 1 0 0 1-1 1H3a1 1 0 0 1-1-1V1a1 1 0 0 1 1-1zm0 2v8h6V2z"/></svg>0123 456 789</li>
      <li><svg viewBox="0 0 12 12"><path d="M0 2h12v8H0zm1 1v.5L6 7l5-3.5V3z"/></svg>youremail@mail.com</li>
      <li><svg viewBox="0 0 12 12"><path d="M6 0a6 6 0 1 0 0 12A6 6 0 0 0 6 0zm0 1.2a4.8 4.8 0 0 1 4.7 4.2H1.3A4.8 4.8 0 0 1 6 1.2zm-4.7 5.4h9.4a4.8 4.8 0 0 1-9.4 0z"/></svg>www.yourwebsite.com</li>
    </ul>
    <div class="card__address">address (street address<br>suite number, city, state, zip</div>
    <div class="card__base"></div>
    <div class="card__base-accent"></div>
  </section>
</main>
</body>
</html>
```